Verdo Studios Business Card

Business card for video production company, I want to give the impression of quality, It has to stand out for its design; it has to be easily readable and please avoid any extravaganza!. I'm looking for a first impression, then the card goes to the trash.

You guys have complete freedom of design! background color, logo colors etc
you can choose one side card or two sided, die cut also a possibility .
Just let me know for what kind of card is your design.
In the files you will find the logo .ai to modify it.

One of the differences between the ambiguous terms Filmmaker and videographer is that filmmaking is more arty, we tend to leave backgrounds out of focus, we create different layers or points of attention with our lens.

Logo
Filmmaking Done Right
www.verdostudios-example.com
www.facebook.com/verdostudios-example
tomas@verdostudios-example.com
555-318-6092
Add QR Code

```html
<!DOCTYPE html>
<html lang="en">
<head>
<meta charset="utf-8">
<title>Verdo Studios – Business Card</title>
<link rel="stylesheet" href="https://fonts.googleapis.com/css2?family=Michroma&family=Quicksand:wght@500&display=swap">
<style>
  :root {
    --paper: #ffffff;
    --ink: #141414;
    --band: #1a1a1a;
    --on-band: #ffffff;
  }
  * { margin: 0; padding: 0; box-sizing: border-box; }
  html, body { width: 1200px; height: 694px; overflow: hidden; background: var(--paper); }
  .card { position: relative; width: 1200px; height: 694px; background: var(--paper); }
  .rule { position: absolute; left: 0; width: 1200px; background: var(--band); }
  .rule--top { top: 130px; height: 14px; }
  .rule--bottom { top: 394px; height: 18px; }
  .band { position: absolute; left: 0; top: 152px; width: 1200px; height: 232px; background: var(--band); }
  .brand-mark { position: absolute; left: 96px; top: 178px; width: 180px; height: 180px; background: var(--on-band); }
  .brand-name {
    position: absolute; left: 440px; top: 200px;
    font-family: "Michroma", sans-serif; font-size: 46px; letter-spacing: 3px;
    color: var(--on-band); text-transform: uppercase; white-space: nowrap;
  }
  .tagline {
    position: absolute; left: 610px; top: 284px;
    font-family: "Quicksand", sans-serif; font-weight: 500; font-size: 36px;
    color: var(--on-band); white-space: nowrap;
  }
  .contact { position: absolute; left: 76px; top: 432px; list-style: none;
    font-family: "Quicksand", sans-serif; font-weight: 500; font-size: 32px; color: var(--ink); }
  .contact li { height: 51px; line-height: 51px; white-space: nowrap; }
</style>
</head>
<body>
  <main class="card">
    <div class="rule rule--top"></div>
    <div class="band"></div>
    <div class="rule rule--bottom"></div>
    <div class="brand-mark"></div>
    <h1 class="brand-name">Verdo Studios</h1>
    <p class="tagline">Filmmaking Done Right</p>
    <ul class="contact">
      <li>Phone: 555-318-6092</li>
      <li>Email: tomas@verdostudios-example.com</li>
      <li>Facebook: /verdostudios-example</li>
      <li>www.verdostudios-example.com</li>
    </ul>
  </main>
</body>
</html>
```